Letter and Envelope Design For Larchmont Realty

Please design a letter and an envelope incorporating our logo (See Attached). We are also launched a business card contest. Since we want them to match, please feel free to submit a design for both the business card and also the letter design and envelope.

Requirements
Must have
• The envelope, the letter and the business cards must match somehow connecting the designs. We want them to have something that holds them together besides the logo.

```html
<!DOCTYPE html>
<html lang="en">
<head>
<meta charset="utf-8">
<title>Larchmont Realty Stationery</title>
<link rel="stylesheet" href="https://fonts.googleapis.com/css2?family=Montserrat:wght@400;500;600&display=swap">
<style>
:root{
  --navy:#2d2f8e;
  --grey:#6d6e71;
  --ink:#3a3a3c;
  --paper:#ffffff;
  --canvas:#eeeeee;
  --stage:#595a5c;
  --card-dark:#1d1d1f;
}
*{box-sizing:border-box;margin:0;padding:0}
html,body{width:1200px;height:3228px;overflow:hidden}
body{background:var(--canvas);font-family:'Montserrat',sans-serif;color:var(--ink);position:relative}
.sheet{position:absolute;background:var(--paper);box-shadow:0 2px 10px rgba(0,0,0,.12);overflow:hidden}
.brand{display:flex;align-items:center;gap:8px;color:var(--navy);font-weight:600;letter-spacing:.08em;text-transform:uppercase;white-space:nowrap}
.brand-dot{border:2px solid var(--navy);border-radius:50%;flex:none}
.band{position:absolute;left:0;right:0;bottom:0;height:10px;background:var(--navy)}
.band::after{content:"";position:absolute;right:0;top:0;bottom:0;width:38%;background:var(--grey);clip-path:polygon(3% 0,100% 0,100% 100%,0 100%)}
address{font-style:normal}

/* Letterhead */
.letterhead{left:240px;top:50px;width:720px;height:1000px}
.lh-header{position:absolute;left:50px;right:50px;top:45px;display:flex;justify-content:space-between;align-items:center;font-size:9px;line-height:1.5}
.lh-header .brand{font-size:17px}
.lh-header .brand-dot{width:34px;height:34px}
.contact-list{list-style:none}
.contact-list li{display:flex;align-items:center;gap:6px;white-space:nowrap}
.contact-list svg{width:10px;height:10px;flex:none}
.lh-rule{position:absolute;left:0;right:0;top:110px;height:1px;background:#dcdcdc}
.lh-body{position:absolute;left:50px;right:50px;top:150px;font-size:9.5px;line-height:1.7}
.lh-to{display:flex;justify-content:space-between}
.lh-name{color:var(--navy);font-weight:600;font-size:11px}
.lh-body p{margin-top:18px}
.lh-sign{margin-top:30px;display:flex;flex-direction:column;align-items:flex-start}
.sign-line{display:block;width:70px;height:24px;margin:4px 0}

/* Envelopes */
.env{width:480px;height:220px}
.env-front{left:100px;top:1200px}
.env-back{left:620px;top:1200px}
.env-front .brand{position:absolute;left:24px;top:22px;font-size:11px}
.env-front .brand-dot{width:22px;height:22px}
.env-address{position:absolute;left:24px;bottom:34px;font-size:7px;line-height:1.6;border-left:2px solid var(--navy);padding-left:6px}
.flap{position:absolute;left:0;top:0;width:100%;height:95px}
.big{width:480px;height:640px;top:1570px}
.big-back{left:100px}
.big-front{left:620px}
.big-back .flap{height:60px}
.big-front .brand{position:absolute;left:28px;top:28px;font-size:11px}
.big-front .brand-dot{width:22px;height:22px}
.big-front .env-address{left:28px;bottom:40px}

/* Business cards */
.stage{position:absolute;left:0;top:2270px;width:1200px;height:958px;background:var(--stage)}
.card{position:absolute;width:440px;height:250px;top:2620px;box-shadow:0 6px 18px rgba(0,0,0,.35);overflow:hidden}
.card-front{left:130px;background:var(--card-dark);display:flex;align-items:center;justify-content:center}
.card-front .brand{color:#2b2b2e;font-size:22px}
.card-front .brand-dot{border-color:#2b2b2e;width:40px;height:40px}
.card-back{left:630px;background:var(--paper)}
.card-back .brand{position:absolute;left:28px;top:128px;font-size:15px;line-height:1.25}
.card-back .brand-dot{width:34px;height:34px}
.card-person{position:absolute;left:250px;top:34px;font-size:8px;line-height:1.6;width:170px}
.card-person .lh-name{font-size:12px;text-transform:uppercase;letter-spacing:.04em}
.card-person .contact-list{margin-top:10px}
</style>
</head>
<body>

<svg width="0" height="0" style="position:absolute">
  <defs>
    <symbol id="icon-phone" viewBox="0 0 10 10"><circle cx="5" cy="5" r="5" fill="#2d2f8e"/><path d="M3.3 2.6l1 1-.5.6a3 3 0 0 0 2 2l.6-.5 1 1-.7.7C5 7.4 2.6 5 2.6 3.3z" fill="#fff"/></symbol>
    <symbol id="icon-mail" viewBox="0 0 10 10"><circle cx="5" cy="5" r="5" fill="#2d2f8e"/><rect x="2.6" y="3.3" width="4.8" height="3.4" fill="none" stroke="#fff" stroke-width=".6"/><path d="M2.6 3.3L5 5.2l2.4-1.9" fill="none" stroke="#fff" stroke-width=".6"/></symbol>
    <symbol id="icon-web" viewBox="0 0 10 10"><circle cx="5" cy="5" r="5" fill="#2d2f8e"/><circle cx="5" cy="5" r="2.6" fill="none" stroke="#fff" stroke-width=".6"/><path d="M2.4 5h5.2M5 2.4c-1.4 1.5-1.4 3.7 0 5.2M5 2.4c1.4 1.5 1.4 3.7 0 5.2" fill="none" stroke="#fff" stroke-width=".5"/></symbol>
    <symbol id="icon-pin" viewBox="0 0 10 10"><circle cx="5" cy="5" r="5" fill="#2d2f8e"/><path d="M5 2.3a1.9 1.9 0 0 0-1.9 1.9C3.1 5.6 5 7.7 5 7.7s1.9-2.1 1.9-3.5A1.9 1.9 0 0 0 5 2.3z" fill="#fff"/></symbol>
  </defs>
</svg>

<section class="sheet letterhead">
  <header class="lh-header">
    <div class="brand"><span class="brand-dot"></span>Larchmont Realty</div>
    <address>Larchmont Realty<br>220 Birch Lane, Suite 4<br>Brookfield, RI 02900</address>
    <ul class="contact-list">
      <li><svg><use href="#icon-phone"/></svg>(401) 555-0182</li>
      <li><svg><use href="#icon-mail"/></svg>info@larchmontrealty.com</li>
      <li><svg><use href="#icon-web"/></svg>www.larchmontrealty.com</li>
    </ul>
  </header>
  <div class="lh-rule"></div>
  <div class="lh-body">
    <div class="lh-to">
      <div><div class="lh-name">Daniel Hartwell</div>Manager</div>
      <div>Date: 12/1/2016</div>
    </div>
    <p>Ellis Graham Company<br>18 Harbor Road, Brookfield 02900</p>
    <p>Thank you for your recent inquiry about listings in the Brookfield area. We have prepared a short summary of homes that match your needs and budget, along with notes on local schools and transit.</p>
    <p>Our team will be glad to arrange viewings at a time that suits you. Please let us know which properties interest you most.</p>
    <p>We look forward to helping you find your next home.</p>
    <div class="lh-sign">
      <span>Sincerely,</span>
      <svg class="sign-line" viewBox="0 0 70 24"><path d="M2 18c6-10 9-12 10-6s4 4 7-2 5 6 9 2 8-8 12-4 10 2 14 0" fill="none" stroke="#3a3a3c" stroke-width="1"/></svg>
      <span>Daniel Hartwell</span>
    </div>
  </div>
  <div class="band"></div>
</section>

<section class="sheet env env-front">
  <div class="brand"><span class="brand-dot"></span>Larchmont Realty</div>
  <address class="env-address">Larchmont Realty<br>220 Birch Lane, Suite 4<br>Brookfield, RI 02900</address>
  <div class="band" style="height:7px"></div>
</section>

<section class="sheet env env-back">
  <svg class="flap" viewBox="0 0 480 95" preserveAspectRatio="none"><path d="M0 0H480V22L300 92Q240 100 180 92L0 22Z" fill="#2d2f8e"/></svg>
</section>

<section class="sheet big big-back">
  <svg class="flap" viewBox="0 0 480 60" preserveAspectRatio="none"><rect width="480" height="60" fill="#2d2f8e"/></svg>
</section>

<section class="sheet big big-front">
  <div class="brand"><span class="brand-dot"></span>Larchmont Realty</div>
  <address class="env-address">Larchmont Realty<br>220 Birch Lane, Suite 4<br>Brookfield, RI 02900</address>
  <div class="band" style="height:7px"></div>
</section>

<div class="stage"></div>

<section class="card card-front">
  <div class="brand"><span class="brand-dot"></span>Larchmont Realty</div>
</section>

<section class="card card-back">
  <div class="brand"><span class="brand-dot"></span><span>Larchmont<br>Realty</span></div>
  <div class="card-person">
    <div class="lh-name">Daniel Hartwell</div>
    Manager
    <ul class="contact-list">
      <li><svg><use href="#icon-pin"/></svg>220 Birch Lane, Brookfield</li>
      <li><svg><use href="#icon-phone"/></svg>(401) 555-0182</li>
      <li><svg><use href="#icon-mail"/></svg>info@larchmontrealty.com</li>
      <li><svg><use href="#icon-web"/></svg>www.larchmontrealty.com</li>
    </ul>
  </div>
  <div class="band" style="height:8px"></div>
</section>

</body>
</html>
```